Do me a Simple layout and Blow the stockings off my clients!!

I am a Personal Stylist focusing on helping women/mothers needing to revamp their wardrobe and feel confident and fresh again. I'm receiving very positive feedback and growing interest in the services I offer. I provide a 'Client Profile' as part of that service in a word document (saved as PDF). What I'm needing is to turn the average looking word document into a modern, funky and professional document template. I have a business logo and copy.
The template should be fluid, easy to update and communicate sassy, funky and professional.

Target Market(s)

Females 25-65.

Industry/Entity Type

Business

Font styles to use
Other font styles liked:
• HelveticaNeue Condensed, or Raleway

Requirements
Must have
• Colours and styles consistent with logo, and fashion industry.
• Interesting and emotive elements around the content.
• Create clear 'sections' with high impact (full coloured page with single, simple section heading ?)
Nice to have
• Ability to feature 'subjects' photos in interesting ways through out the document.
• Don't just stick with portrait layout, landscape is fine too.
Should not have
• Not too busy - less is more.

```html
<!DOCTYPE html>
<html lang="en">
<head>
<meta charset="utf-8">
<title>Polish &amp; Pearls – Client Style Profile</title>
<link href="https://fonts.googleapis.com/css2?family=Cinzel:wght@400;600&family=Questrial&family=Raleway:ital,wght@0,300;0,400;0,600;1,300;1,600&display=swap" rel="stylesheet">
<style>
  :root {
    --pink: #e0288f;
    --pink-soft: #f08cbf;
    --plum: #9b5b98;
    --plum-deep: #7e3f82;
    --mauve: #c79bc6;
    --blush: #f4e4ef;
    --paper: #fdf7fb;
    --ink: #333033;
    --ink-soft: #6b6570;
    --line: #d9d2da;
  }
  * { box-sizing: border-box; margin: 0; padding: 0; }
  html, body { width: 1200px; height: 630px; overflow: hidden; background: #ffffff; }
  .canvas { position: relative; width: 1200px; height: 630px; overflow: hidden; background: #ffffff; font-family: "Questrial", sans-serif; color: var(--ink); }

  /* Page panels */
  .page {
    position: absolute; overflow: hidden;
    background: linear-gradient(180deg, var(--mauve) 0%, #e7cbe2 28%, var(--blush) 55%, #ead0e4 85%, #d9b3d4 100%);
  }
  .page::after {
    content: ""; position: absolute; left: 0; right: 0; bottom: 0; height: 14px;
    background: linear-gradient(90deg, var(--plum-deep), var(--plum), #b77fb5);
  }
  .page--cover { left: 152px; top: 8px; width: 456px; height: 322px;
    background: radial-gradient(ellipse at 40% 45%, #f6e6f0 0%, #dcb6d6 45%, #b47bb4 100%); }
  .page--cover::after { height: 16px; }
  .page--report { left: 616px; top: 8px; width: 428px; height: 322px; }
  .page--notes { left: 0; top: 338px; width: 385px; height: 284px; }
  .page--finds { left: 393px; top: 338px; width: 397px; height: 284px; }
  .page--picks { left: 800px; top: 338px; width: 400px; height: 284px; }

  .frame {
    position: absolute; border: 2px solid var(--pink); border-radius: 22px;
    background: rgba(255,255,255,0.55);
  }

  /* Brand mark */
  .brand { position: absolute; text-align: right; }
  .brand__name { font-family: "Raleway", sans-serif; font-weight: 400; color: var(--pink); line-height: 1; }
  .brand__person { font-family: "Raleway", sans-serif; font-weight: 400; color: var(--ink-soft); letter-spacing: 0.08em; margin-top: 3px; white-space: nowrap; }
  .brand--small { width: 80px; }
  .brand--small .brand__name { font-size: 15px; white-space: nowrap; }
  .brand--small .brand__person { font-size: 5.5px; }

  /* Cover */
  .cover-plaque {
    position: absolute; left: 58px; top: 50px; width: 292px; height: 218px;
    background: #ffffff; border: 7px solid var(--pink); border-radius: 40px;
    box-shadow: 0 0 0 2px #ffffff, 0 0 0 4px var(--pink-soft);
    display: flex; flex-direction: column; justify-content: center; align-items: center;
  }
  .cover-plaque .brand__name { font-size: 50px; text-align: center; line-height: 1.05; }
  .cover-plaque .brand__person { font-size: 13px; margin-top: 14px; color: var(--ink-soft); align-self: flex-end; margin-right: 42px; }
  .cover-figure {
    position: absolute; left: 338px; top: 6px; width: 104px; height: 296px;
    border-radius: 50px 50px 20px 20px;
    background: linear-gradient(180deg, rgba(255,255,255,0.8) 0%, #f4dde9 35%, #bfe0d6 50%, #d8b9de 72%, rgba(255,255,255,0.6) 100%);
  }

  /* Report */
  .report-title { position: absolute; left: 110px; width: 220px; top: 42px; text-align: center; font-family: "Cinzel", serif; font-weight: 400; font-size: 14px; color: var(--pink); letter-spacing: 0.03em; white-space: nowrap; }
  .report { position: absolute; left: 46px; top: 76px; width: 330px; font-size: 6.1px; line-height: 1.45; }
  .report__row { display: grid; grid-template-columns: 114px 1fr; margin-bottom: 10px; }
  .report__row--tight { grid-template-columns: 44px 1fr; margin-bottom: 1px; }
  .report__label { color: var(--pink); font-weight: 400; }
  .report__list { list-style: none; }
  .report__list li::before { content: "• "; }

  /* Notes */
  .section-title { position: absolute; left: 40px; width: 250px; text-align: center; font-family: "Cinzel", serif; font-size: 11px; color: var(--pink); letter-spacing: 0.02em; white-space: nowrap; }
  .note { position: absolute; left: 22px; width: 345px; height: 72px; background: rgba(255,255,255,0.9); display: flex; align-items: center; gap: 12px; padding: 0 10px; }
  .note__photo { flex: 0 0 76px; height: 60px; border: 2px solid var(--pink); background: linear-gradient(135deg, #ffffff, #f6e9f1); }
  .note__text { font-family: "Raleway", sans-serif; font-style: italic; font-weight: 300; font-size: 5.4px; line-height: 1.5; color: var(--ink-soft); }
  .note__text::before { content: "\201C\00a0"; font-weight: 600; font-style: normal; }
  .note__text::after { content: "\00a0\201D"; font-weight: 600; font-style: normal; }

  /* Product finds */
  .finds-intro { position: absolute; left: 30px; top: 34px; width: 262px; text-align: center; font-family: "Raleway", sans-serif; font-style: italic; font-weight: 600; font-size: 7px; line-height: 1.35; color: var(--ink); }
  .card { position: absolute; background: #ffffff; border: 2px solid var(--pink-soft); display: flex; gap: 6px; padding: 6px; }
  .card__photo { flex: 0 0 42%; height: 100%; background: linear-gradient(180deg, #eeeeee, #cfcfd4); }
  .card__photo--stripe { background: linear-gradient(180deg, #e9e9ec, #4a4a55 50%, #e9e9ec); }
  .card__photo--navy { background: linear-gradient(180deg, #d9dbe5, #2f3552); }
  .card__photo--grey { background: linear-gradient(180deg, #e3e3e3, #9a9a9d); }
  .card__photo--cream { background: linear-gradient(180deg, #faf6ef, #e8dfd2); }
  .card__photo--floral { background: linear-gradient(180deg, #3a3a4a, #c0576e 55%, #2b2b39); }
  .card__info { flex: 1; min-width: 0; display: flex; flex-direction: column; gap: 3px; font-size: 4.6px; color: var(--ink); }
  .card__name { font-weight: 400; letter-spacing: 0.05em; font-size: 5px; }
  .card__price { color: var(--ink-soft); }
  .card__line { height: 2px; background: var(--line); width: 80%; }
  .card__line--short { width: 45%; }
  .card__button { width: 28px; height: 7px; background: #1e1e1e; margin-top: 3px; }
</style>
</head>
<body>
<main class="canvas">

  <section class="page page--cover" aria-label="Cover">
    <div class="cover-plaque">
      <p class="brand__name">Polish &amp;<br>Pearls</p>
      <p class="brand__person">MARA LINDQVIST</p>
    </div>
    <div class="cover-figure" role="img" aria-label="Fashion illustration of a woman in a mint top and lilac skirt"></div>
  </section>

  <section class="page page--report" aria-label="Style analysis report">
    <div class="frame" style="left:10px; top:22px; width:405px; height:276px;"></div>
    <div class="brand brand--small" style="right:16px; top:20px;">
      <p class="brand__name">Polish &amp;<br>Pearls</p>
      <p class="brand__person">MARA LINDQVIST</p>
    </div>
    <h2 class="report-title">STYLE ANALYSIS REPORT</h2>
    <div class="report">
      <div class="report__row report__row--tight"><span class="report__label">Client</span><span>: Jess</span></div>
      <div class="report__row report__row--tight" style="margin-bottom:12px;"><span class="report__label">Body Shape</span><span>: The Brick, shorter waist.</span></div>
      <div class="report__row">
        <span class="report__label">Main characteristics:</span>
        <ul class="report__list">
          <li>Broad shoulders</li>
          <li>Hips inline with shoulders</li>
          <li>No shapely waist line</li>
          <li>Possibly larger (ish) thighs</li>
        </ul>
      </div>
      <div class="report__row">
        <span class="report__label">Main goals in dressing ‘The Brick’:</span>
        <ul class="report__list">
          <li>Create curves using shapely, flowing pieces</li>
          <li>Look for curved edges on garments</li>
          <li>Sweetheart necklines will instantly create a more shapely start to your upper body</li>
          <li>Use patterns to accentuate your best areas and detract from others.</li>
          <li>Use stripes of varying sizes, to create a shapely illusion</li>
          <li>For accessories look for curvy jewelry and handbags</li>
        </ul>
      </div>
      <div class="report__row">
        <span class="report__label">Styles to avoid:</span>
        <ul class="report__list">
          <li>Square cut or boxed edge jackets</li>
          <li>Short skirts (mini) or shorts which will cut you off mid thigh</li>
          <li>Box pleats or pleats at the front of trousers</li>
          <li>Look for shoes that add to the flow of your garment, nothing too solid, or chunky</li>
        </ul>
      </div>
      <div class="report__row">
        <span class="report__label">Celebrity ‘Bricks’ &nbsp;&nbsp;:</span>
        <span>Lena Marsh, Tilly Rowe, Carla Vance</span>
      </div>
    </div>
  </section>

  <section class="page page--notes" aria-label="Notes from your styling session">
    <div class="frame" style="left:10px; top:18px; width:365px; height:240px; background:transparent;"></div>
    <div class="brand brand--small" style="right:18px; top:14px;">
      <p class="brand__name">Polish &amp;<br>Pearls</p>
      <p class="brand__person">MARA LINDQVIST</p>
    </div>
    <h2 class="section-title" style="top:38px;">NOTES FROM YOUR STYLING SESSION</h2>
    <div class="note" style="top:84px;">
      <div class="note__photo" role="img" aria-label="Client photo in outfit one"></div>
      <p class="note__text">Ok, I’ll be short and sweet: Terrible! The sleeves do nothing for the tops of your arms, the seam across the middle of your waist is cutting you in two and the length of the top does nothing but draw attention to your crotch… thank goodness we put this one back on the hanger!</p>
    </div>
    <div class="note" style="top:166px; flex-direction:row-reverse;">
      <div class="note__photo" role="img" aria-label="Client photo in outfit two"></div>
      <p class="note__text">Sophistication in a pair of heels! This outfit is so chic and elegant; it could be transformed from a work outfit to a daytime outfit, to a nighttime outfit, by changing up accessories. A jacket (eg. denim jacket or smart blazer) to a fabulous pair of heels or a wedge! These trousers are great, look at how long and slender they make your legs look. They sit perfectly on your hips and then don’t cling anywhere. The straight/bootleg cut works really well for you. This outfit has to be a massive winner!</p>
    </div>
  </section>

  <section class="page page--finds" aria-label="Online finds">
    <div class="frame" style="left:8px; top:14px; width:381px; height:256px;"></div>
    <div class="brand brand--small" style="right:16px; top:18px;">
      <p class="brand__name">Polish &amp;<br>Pearls</p>
      <p class="brand__person">MARA LINDQVIST</p>
    </div>
    <p class="finds-intro">I’ve also had quick surf on the net to see if there was anything worth looking at, or even just for you to use as a guide. I looked through Maison Ferro, Wrenly and Tacks. These are just a few examples</p>

    <div class="card" style="left:22px; top:70px; width:175px; height:92px;">
      <div class="card__photo card__photo--stripe" role="img" aria-label="Product photo: striped knit dress"></div>
      <div class="card__info"><span class="card__name">STRIPE KNIT DRESS</span><span class="card__price">$89.95</span><span class="card__line"></span><span class="card__line card__line--short"></span><span class="card__line"></span><span class="card__button"></span></div>
    </div>
    <div class="card" style="left:203px; top:70px; width:175px; height:92px;">
      <div class="card__photo card__photo--navy" role="img" aria-label="Product photo: navy striped maxi dress"></div>
      <div class="card__info"><span class="card__name">STRIPE MAXI DRESS</span><span class="card__price">$129.95</span><span class="card__line"></span><span class="card__line card__line--short"></span><span class="card__line"></span><span class="card__button"></span></div>
    </div>
    <div class="card" style="left:22px; top:168px; width:175px; height:94px;">
      <div class="card__photo card__photo--grey" role="img" aria-label="Product photo: grey slub knit jumper"></div>
      <div class="card__info"><span class="card__name">SLUB KNIT</span><span class="card__price">$99.95</span><span class="card__line"></span><span class="card__line card__line--short"></span><span class="card__line"></span><span class="card__button"></span></div>
    </div>
    <div class="card" style="left:203px; top:168px; width:175px; height:94px;">
      <div class="card__photo card__photo--grey" role="img" aria-label="Product photo: grey striped blazer"></div>
      <div class="card__info"><span class="card__name">STRIPE BLAZER</span><span class="card__price">$149.95</span><span class="card__line"></span><span class="card__line card__line--short"></span><span class="card__line"></span><span class="card__button"></span></div>
    </div>
  </section>

  <section class="page page--picks" aria-label="More picks">
    <div class="frame" style="left:10px; top:14px; width:380px; height:256px;"></div>
    <div class="brand brand--small" style="right:16px; top:18px;">
      <p class="brand__name">Polish &amp;<br>Pearls</p>
      <p class="brand__person">MARA LINDQVIST</p>
    </div>

    <div class="card" style="left:50px; top:62px; width:132px; height:94px;">
      <div class="card__photo card__photo--grey" role="img" aria-label="Product photo: striped linen henley"></div>
      <div class="card__info"><span class="card__name">STRIPE LINEN HENLEY</span><span class="card__price">$59.95</span><span class="card__line"></span><span class="card__line card__line--short"></span><span class="card__button"></span></div>
    </div>
    <div class="card" style="left:188px; top:62px; width:132px; height:94px;">
      <div class="card__photo card__photo--navy" role="img" aria-label="Product photo: navy striped tee"></div>
      <div class="card__info"><span class="card__name">MARINA STRIPE TEE</span><span class="card__price">$49.95</span><span class="card__line"></span><span class="card__line card__line--short"></span><span class="card__button"></span></div>
    </div>
    <div class="card" style="left:30px; top:164px; width:112px; height:94px;">
      <div class="card__photo card__photo--cream" role="img" aria-label="Product photo: cream knit cardigan"></div>
      <div class="card__info"><span class="card__name">CREAM KNIT CARDIGAN</span><span class="card__price">$79.95</span><span class="card__line"></span><span class="card__line card__line--short"></span></div>
    </div>
    <div class="card" style="left:146px; top:164px; width:118px; height:94px;">
      <div class="card__photo card__photo--floral" role="img" aria-label="Product photo: dark floral print top"></div>
      <div class="card__info"><span class="card__name">FLORAL PRINT TOP</span><span class="card__line"></span><span class="card__line card__line--short"></span></div>
    </div>
    <div class="card" style="left:268px; top:164px; width:114px; height:94px;">
      <div class="card__photo card__photo--navy" role="img" aria-label="Product photo: navy draped jersey tee"></div>
      <div class="card__info"><span class="card__name">DRAPED JERSEY TEE</span><span class="card__line"></span><span class="card__line card__line--short"></span><span class="card__button"></span></div>
    </div>
  </section>

</main>
</body>
</html>
```